VELTA CORE

I am in this industry for last 15 years we have done lots of commercial site like we work with BRAVEN costruction, lumo properties, TWD, penwick construction.
We do all domestic and commercial wall and floor tiling, swimming pools, spas, paving, marbles blue stones and muchmore.

Specializing in the wall and floor Tiling, Waterproofing and floor preparations

Industry/Entity Type

Industry

Number of Pages Required

1 page

Font styles to use
Serif
Decorative

Colors

Designer to choose colors to be used in the design.

Requirements
Must have
• domestic and commercial indoor tiling, bathroom tiling and paving pictures
Nice to have
• beautiful bathroom pictures with tile

```html
<!DOCTYPE html>
<html lang="en">
<head>
<meta charset="utf-8">
<title>VELTA CORE – Floor Tiling, Waterproofing and Floor Preparations</title>
<link href="https://fonts.googleapis.com/css2?family=Lato:wght@400;700;900&display=swap" rel="stylesheet">
<style>
:root{
  --orange:#e0610e;
  --orange-dark:#c4530a;
  --ink:#1f1f1f;
  --text:#555;
  --muted:#8a8a8a;
  --dark:#232323;
  --darker:#1a1a1a;
  --light:#f3f3f3;
  --white:#fff;
}
*{box-sizing:border-box;margin:0;padding:0}
html,body{width:1200px;height:4972px;overflow:hidden}
body{font-family:"Lato",Arial,sans-serif;color:var(--text);background:var(--white);position:relative}
section,header,nav,footer{position:relative;display:block;width:1200px;overflow:visible}
.abs{position:absolute}
.btn{position:absolute;display:flex;align-items:center;justify-content:center;background:var(--orange);color:var(--white);font-size:14px;font-weight:700;border-radius:20px}
.photo{position:absolute}
p{font-size:13px;line-height:22px}

/* top bar */
.topbar{height:40px;background:var(--darker);color:#ccc;font-size:12px}
.topbar .contact{left:99px;top:12px;display:flex;gap:28px}
.topbar .contact span{display:flex;align-items:center;gap:8px}
.topbar .social{right:99px;top:12px;display:flex;gap:12px;align-items:center}
.topbar .dot{width:10px;height:10px;border-radius:50%;background:#888}

/* nav */
.nav{height:93px;background:var(--white)}
.brand{left:99px;top:30px;font-size:30px;font-weight:900;color:var(--ink);letter-spacing:1px;line-height:36px}
.menu{right:99px;top:38px;display:flex;gap:34px;font-size:13px;font-weight:700;color:var(--ink)}
.menu .active{color:var(--orange)}

/* hero */
.hero{height:547px;overflow:hidden}
.hero .photo{inset:0;background:linear-gradient(180deg,#5a4436 0%,#7a6352 45%,#3b2f28 100%)}
.hero .shade{position:absolute;inset:0;background:rgba(0,0,0,.35)}
.hero h1{position:absolute;left:0;right:0;top:225px;text-align:center;color:var(--white);font-size:52px;font-weight:900;letter-spacing:2px;line-height:60px}
.hero .tagline{position:absolute;left:0;right:0;top:300px;text-align:center;color:var(--white);font-size:25px;line-height:30px}
.hero .btn{left:515px;top:366px;width:170px;height:40px}
.hero .arrow{position:absolute;top:240px;width:40px;height:40px;border-radius:50%;background:var(--white);display:flex;align-items:center;justify-content:center}
.hero .wave{position:absolute;left:0;bottom:-1px}

/* about */
.about{height:414px}
.eyebrow{font-size:18px;font-weight:900;color:var(--ink)}
.about .eyebrow{left:99px;top:44px}
.about h2{position:absolute;left:99px;top:72px;font-size:30px;font-weight:900;color:var(--ink)}
.about p{position:absolute;left:99px;width:510px}
.about .btn{left:99px;top:280px;width:136px;height:40px}
.about .photo{left:663px;top:49px;width:431px;height:299px;background:linear-gradient(135deg,#b0703d,#7c4a28 60%,#5a3520)}
.play{position:absolute;left:195px;top:129px;width:42px;height:42px;border-radius:50%;background:rgba(0,0,0,.75);display:flex;align-items:center;justify-content:center}

/* dark tiling */
.tiling{height:663px;background:linear-gradient(180deg,#2a2a2a,#1c1c1c)}
.tiling .topwave{position:absolute;left:0;top:-1px}
.tiling h3{position:absolute;font-size:18px;font-weight:900;color:var(--white)}
.tiling p{position:absolute;width:460px;color:#bbb}
.tiling .more{position:absolute;font-size:13px;color:#ddd;text-decoration:underline}
.tiling .dom{left:99px;top:282px;width:448px;height:258px;background:linear-gradient(135deg,#d9d9d9,#a9b1b5 55%,#6f7478)}
.tiling .com{left:653px;top:176px;width:447px;height:258px;background:linear-gradient(180deg,#5a1a1a 0%,#b32020 40%,#c9c9c9 75%,#8f8f8f)}

/* specialising */
.special{height:457px}
.special h2{position:absolute;left:0;right:0;top:56px;text-align:center;font-size:30px;font-weight:900;color:var(--ink)}
.skill{position:absolute;top:142px;width:240px;text-align:center}
.skill .ring{margin:0 auto;width:114px;height:114px;border-radius:50%;background:var(--orange);display:flex;align-items:center;justify-content:center}
.skill .inner{width:90px;height:90px;border-radius:50%;border:3px solid var(--white);display:flex;align-items:center;justify-content:center}
.skill h4{margin-top:26px;font-size:17px;font-weight:900;color:var(--ink)}
.skill p{margin-top:10px;font-size:12px;line-height:21px}

/* quote */
.quote{height:332px;background:linear-gradient(90deg,#2a2a2a,#3a3836 60%,#242424)}
.quote h2{position:absolute;left:99px;top:60px;font-size:30px;font-weight:700;color:var(--white)}
.quote p{position:absolute;left:99px;top:120px;width:600px;color:#ccc;font-size:12px;line-height:21px}
.quote .btn{left:99px;top:230px;width:112px;height:38px}
.form{position:absolute;left:796px;top:-16px;width:314px;height:355px;z-index:3}
.form label{position:absolute;left:24px;font-size:13px;font-weight:900;color:var(--white)}
.form .field{position:absolute;left:24px;width:256px;height:30px;background:var(--white);font-size:12px;color:#777;padding:8px 12px}
.form .send{position:absolute;left:24px;top:254px;width:130px;height:34px;border:2px solid var(--white);border-radius:18px;color:var(--white);font-size:13px;font-weight:700;display:flex;align-items:center;justify-content:center}

/* gallery */
.gallery{height:786px}
.gallery h2{position:absolute;left:0;right:0;top:46px;text-align:center;font-size:30px;font-weight:900;color:var(--ink)}
.tile{position:absolute;overflow:hidden}
.tile .cap{position:absolute;left:0;right:0;height:40px;background:rgba(0,0,0,.45);color:var(--white);font-size:17px;display:flex;align-items:center;justify-content:center}

/* blog */
.blog{height:580px;background:linear-gradient(180deg,#262626,#1d1d1d)}
.blog h2{position:absolute;left:0;right:0;top:46px;text-align:center;font-size:30px;font-weight:900;color:var(--white)}
.card{position:absolute;top:126px;width:242px;height:288px;background:var(--white)}
.card .photo{left:0;top:0;width:242px;height:199px}
.card .band{position:absolute;left:0;top:199px;width:242px;height:89px;text-align:center;padding-top:26px}
.card h5{font-size:15px;font-weight:900;color:var(--orange)}
.card .date{font-size:11px;color:var(--muted);margin-top:6px}
.card.featured .band{background:var(--orange)}
.card.featured h5,.card.featured .date{color:var(--white)}
.blog .btn{left:99px;top:455px;width:124px;height:36px;font-size:13px}
.blog .botwave{position:absolute;left:0;bottom:-1px}

/* testimonial */
.testimonial{height:613px}
.testimonial .qmark{position:absolute;font-size:150px;font-weight:900;color:#eee;line-height:1}
.testimonial h2{position:absolute;left:0;right:0;top:96px;text-align:center;font-size:30px;font-weight:900;color:var(--ink)}
.testimonial p{position:absolute;left:310px;width:580px;top:196px;text-align:center;font-size:12px;line-height:22px;color:var(--muted)}
.avatar{position:absolute;left:567px;top:359px;width:66px;height:66px;border-radius:50%;background:linear-gradient(180deg,#c9ced6,#6f7784)}
.testimonial .name{position:absolute;left:0;right:0;top:448px;text-align:center;font-size:15px;font-weight:900;color:var(--ink)}
.testimonial .loc{position:absolute;left:0;right:0;top:474px;text-align:center;font-size:12px;color:var(--muted)}
.pager{position:absolute;left:560px;top:520px;width:80px;display:flex;justify-content:space-between;align-items:center}
.pager .sep{width:1px;height:26px;background:#ccc}

/* footer */
.footer{height:447px;background:var(--darker);color:#ccc}
.footer .topwave{position:absolute;left:0;top:-1px}
.footer .brand{left:99px;top:140px;color:var(--white)}
.footer .about-text{position:absolute;left:99px;top:190px;width:320px;font-size:12px;line-height:21px;color:#bbb}
.footer h6{position:absolute;top:146px;font-size:18px;font-weight:700;color:var(--white)}
.footer ul{position:absolute;left:471px;top:195px;list-style:none;font-size:12px;line-height:26px;color:#bbb}
.footer li{display:flex;align-items:center;gap:12px}
.footer .mail{position:absolute;left:812px;top:190px;width:285px;height:38px;background:var(--white);color:#777;font-size:12px;padding:12px}
.footer .subscribe{position:absolute;left:812px;top:238px;width:285px;height:38px;background:var(--orange);color:var(--white);font-size:14px;font-weight:900;display:flex;align-items:center;justify-content:center}
.footer .rule{position:absolute;left:99px;right:99px;top:360px;height:1px;background:#3b3b3b}
.footer .copy{position:absolute;left:99px;top:396px;font-size:12px;color:#aaa}
.footer .links{position:absolute;right:99px;top:396px;font-size:12px;color:#aaa;display:flex;gap:14px}
</style>
</head>
<body>

<header class="topbar">
  <div class="abs contact">
    <span><svg width="12" height="12" viewBox="0 0 24 24"><path fill="#e0610e" d="M6.6 10.8a15 15 0 0 0 6.6 6.6l2.2-2.2c.3-.3.7-.4 1-.2 1.1.4 2.3.6 3.6.6.6 0 1 .4 1 1V20c0 .6-.4 1-1 1A17 17 0 0 1 3 4c0-.6.4-1 1-1h3.5c.6 0 1 .4 1 1 0 1.3.2 2.5.6 3.6.1.3 0 .7-.2 1z"/></svg>(555) 014 268 731</span>
    <span><svg width="13" height="10" viewBox="0 0 26 20"><rect x="1" y="1" width="24" height="18" fill="none" stroke="#e0610e" stroke-width="2"/><path d="M1 1l12 10L25 1" fill="none" stroke="#e0610e" stroke-width="2"/></svg>hello@veltacore.example</span>
  </div>
  <div class="abs social"><span>Stay Connected :</span><i class="dot"></i><i class="dot"></i><i class="dot"></i><i class="dot"></i></div>
</header>

<nav class="nav">
  <div class="abs brand">VELTA CORE</div>
  <div class="abs menu"><span class="active">Home</span><span>About Us</span><span>Services</span><span>Projects</span><span>Blog</span><span>Contact Us</span></div>
</nav>

<section class="hero">
  <div class="photo" role="img" aria-label="Modern living room with tiled wall and timber floor"></div>
  <div class="shade"></div>
  <div class="arrow" style="left:30px"><svg width="14" height="14" viewBox="0 0 14 14"><path d="M9 2L4 7l5 5" fill="none" stroke="#222" stroke-width="2.5"/></svg></div>
  <div class="arrow" style="right:30px"><svg width="14" height="14" viewBox="0 0 14 14"><path d="M5 2l5 5-5 5" fill="none" stroke="#222" stroke-width="2.5"/></svg></div>
  <h1>VELTA CORE</h1>
  <div class="tagline">Floor Tiling, Waterproofing and floor preparations</div>
  <div class="btn">Get Started Now</div>
  <svg class="wave" width="1200" height="150" viewBox="0 0 1200 150"><path d="M0 150 L0 120 C300 140 700 110 1200 20 L1200 150 Z" fill="#fff"/></svg>
</section>

<section class="about">
  <div class="abs eyebrow">ABOUT US</div>
  <h2>WELCOME TO VELTA CORE</h2>
  <p style="top:132px">For fifteen years our crews have laid wall and floor tiles across homes, offices and public spaces. We plan each job with care, prepare every surface properly and finish on time, so the result looks sharp and lasts for years.</p>
  <p style="top:206px">From bathrooms and kitchens to pools, spas and paving, we handle the whole project in house with skilled tilers and trusted suppliers.</p>
  <div class="btn">Read More &gt;&gt;</div>
  <div class="photo" role="img" aria-label="Two tilers laying timber-look floor tiles, seen from above">
    <div class="play"><svg width="14" height="16" viewBox="0 0 14 16"><path d="M1 1l12 7-12 7z" fill="#fff"/></svg></div>
  </div>
</section>

<section class="tiling">
  <svg class="topwave" width="1200" height="60" viewBox="0 0 1200 60"><path d="M0 0 H1200 V20 C800 70 400 -10 0 40 Z" fill="#fff"/></svg>
  <h3 style="left:99px;top:104px">DOMESTIC WALL AND FLOOR TILING</h3>
  <p style="left:99px;top:134px">Bathrooms, kitchens and living areas tiled with clean lines and neat grout. We help you pick tiles that suit your home and your budget.</p>
  <div class="more" style="left:99px;top:232px">Read More</div>
  <div class="photo dom" role="img" aria-label="Bright bathroom with bathtub and glass block wall"></div>
  <div class="photo com" role="img" aria-label="Commercial lobby with red feature wall and polished floor tiles"></div>
  <h3 style="left:653px;top:466px">COMMERCIAL WALL AND FLOOR TILING</h3>
  <p style="left:653px;top:496px">Offices, shops and public spaces tiled to a strict schedule, with durable surfaces made for heavy daily traffic and easy care.</p>
  <div class="more" style="left:653px;top:596px">Read More</div>
</section>

<section class="special">
  <h2>WE ARE SPECIALISING</h2>
  <div class="skill" style="left:89px">
    <div class="ring"><div class="inner"><svg width="44" height="44" viewBox="0 0 44 44"><path d="M22 2L42 22 22 42 2 22Z" fill="#fff"/><path d="M22 12L32 22 22 32 12 22Z M12 22H32 M22 12V32" fill="none" stroke="#e0610e" stroke-width="2"/></svg></div></div>
    <h4>Floor Tiling</h4>
    <p>Level, even floors laid with<br>care in every room, built to<br>last through daily use.</p>
  </div>
  <div class="skill" style="left:351px">
    <div class="ring"><div class="inner"><svg width="40" height="40" viewBox="0 0 40 40"><rect x="3" y="3" width="34" height="34" fill="none" stroke="#fff" stroke-width="3"/><path d="M3 14H37M3 26H37M14 3V14M26 14V26M14 26V37" stroke="#fff" stroke-width="3"/></svg></div></div>
    <h4>Wall Tiling</h4>
    <p>Feature walls and splashbacks<br>set straight and true, with<br>tidy cuts around fittings.</p>
  </div>
  <div class="skill" style="left:613px">
    <div class="ring"><div class="inner"><svg width="42" height="42" viewBox="0 0 42 42"><g stroke="#fff" stroke-width="3" stroke-linecap="round"><path d="M21 3V39M5 12L37 30M5 30L37 12"/></g><circle cx="21" cy="21" r="6" fill="#fff"/></svg></div></div>
    <h4>Waterproofing</h4>
    <p>Sealed membranes under wet<br>areas so showers, decks and<br>pools stay leak free.</p>
  </div>
  <div class="skill" style="left:875px">
    <div class="ring"><div class="inner"><svg width="44" height="44" viewBox="0 0 44 44"><circle cx="22" cy="22" r="19" fill="#fff"/><path d="M8 16C16 20 28 20 36 16M6 26C16 30 28 30 38 26" fill="none" stroke="#e0610e" stroke-width="3"/></svg></div></div>
    <h4>Floor preparations</h4>
    <p>Grinding, levelling and priming<br>so each new surface sits flat<br>and bonds firmly.</p>
  </div>
</section>

<section class="quote">
  <h2>Get A Free Quote &nbsp;From Our Experts</h2>
  <p>Tell us about your project and we will visit the site, measure up and send a clear written quote. No hidden costs, no pressure, just honest advice on the right tiles and the right method for the job.</p>
  <div class="btn">Learn More</div>
  <div class="form">
    <svg class="abs" style="left:0;top:0" width="314" height="355" viewBox="0 0 314 355"><path d="M14 0H300L314 14V341L300 355H14L0 341V14Z" fill="#e0610e"/></svg>
    <label style="top:30px">USERNAME</label>
    <div class="field" style="top:52px">Your Name</div>
    <label style="top:94px">EMAIL</label>
    <div class="field" style="top:116px">Your Email</div>
    <label style="top:158px">MESSAGE</label>
    <div class="field" style="top:180px">Type Your Message</div>
    <div class="send">Send Request</div>
  </div>
</section>

<section class="gallery">
  <h2>OUR GALLERY</h2>
  <div class="tile" style="left:99px;top:123px;width:315px;height:265px;background:linear-gradient(135deg,#e6e6e6,#9a9a9a 60%,#3d3d3d)" role="img" aria-label="Domestic bathroom with wall tiling"><div class="cap" style="top:150px">Domestic &nbsp;wall &nbsp;tiling</div></div>
  <div class="tile" style="left:444px;top:123px;width:312px;height:265px;background:linear-gradient(180deg,#f2f2f2,#cfcfcf 60%,#8c8c8c)" role="img" aria-label="Bright commercial room with wall tiling"><div class="cap" style="top:110px">Commercial wall tiling</div></div>
  <div class="tile" style="left:786px;top:123px;width:311px;height:265px;background:linear-gradient(180deg,#8fb3d6,#a46b45 45%,#3fa7c9 80%,#c9a27a)" role="img" aria-label="Backyard swimming pool beside a brick house"><div class="cap" style="top:166px">Swimming pools</div></div>
  <div class="tile" style="left:99px;top:398px;width:315px;height:321px;background:linear-gradient(180deg,#f3e9d6,#c9a97a 50%,#7d6a55)" role="img" aria-label="Large commercial hall with indoor floor tiling"><div class="cap" style="top:194px">Commercial indoor tiling</div></div>
  <div class="tile" style="left:444px;top:398px;width:312px;height:321px;background:linear-gradient(180deg,#243a5c,#7a4a33 50%,#c46a2a 75%,#5b4a3c)" role="img" aria-label="Stone paved patio with outdoor fireplace at dusk"><div class="cap" style="top:194px">Paving</div></div>
  <div class="tile" style="left:786px;top:398px;width:311px;height:321px;background:linear-gradient(180deg,#f5f5f5,#d9d4cc 55%,#a59d92)" role="img" aria-label="Tiled spa room with bath"><div class="cap" style="top:244px">Spas</div></div>
</section>

<section class="blog">
  <h2>BLOG POST</h2>
  <div class="card" style="left:99px"><div class="photo" style="background:linear-gradient(135deg,#c41e1e,#7a1010 55%,#d8d8d8)" role="img" aria-label="Red feature wall tiling"></div><div class="band"><h5>WALL TILING</h5><div class="date">23 Feb 2017</div></div></div>
  <div class="card featured" style="left:351px"><div class="photo" style="background:linear-gradient(180deg,#eef1f3,#b9c2c7 60%,#7e878c)" role="img" aria-label="Room prepared for new floor tiles"></div><div class="band"><h5>FLOOR PREPARATIONS</h5><div class="date">23 Feb 2017</div></div></div>
  <div class="card" style="left:603px"><div class="photo" style="background:linear-gradient(180deg,#d9c2a0,#9b7a55 55%,#5a8a8c)" role="img" aria-label="Tiled bathroom with sunken bath"></div><div class="band"><h5>BATHROOM TILING</h5><div class="date">23 Feb 2017</div></div></div>
  <div class="card" style="left:855px"><div class="photo" style="background:linear-gradient(180deg,#6c8f6a,#2f8fbf 55%,#c8b89a)" role="img" aria-label="Outdoor swimming pool with tiled surround"></div><div class="band"><h5>SWIMMING POOLS</h5><div class="date">23 Feb 2017</div></div></div>
  <div class="btn">View All Post</div>
  <svg class="botwave" width="1200" height="70" viewBox="0 0 1200 70"><path d="M0 70 V60 C400 70 800 40 1200 0 V70 Z" fill="#fff"/></svg>
</section>

<section class="testimonial">
  <div class="qmark" style="left:560px;top:50px">“</div>
  <h2>WHAT CUSTOMER SAY</h2>
  <p>The team retiled our bathroom and laundry in under a week and left the house spotless. Every tile sits perfectly level, the grout lines are crisp and the shower has stayed dry ever since. They explained each step, kept to the quote and were a pleasure to have around. We will gladly call them again for the patio.</p>
  <div class="qmark" style="left:860px;top:300px;font-size:90px">”</div>
  <div class="avatar" role="img" aria-label="Customer portrait"></div>
  <div class="name">– Dana Morrow</div>
  <div class="loc">- City Location</div>
  <div class="pager">
    <svg width="12" height="14" viewBox="0 0 12 14"><path d="M8 2L3 7l5 5" fill="none" stroke="#333" stroke-width="2"/></svg>
    <span class="sep"></span>
    <svg width="12" height="14" viewBox="0 0 12 14"><path d="M4 2l5 5-5 5" fill="none" stroke="#333" stroke-width="2"/></svg>
  </div>
</section>

<footer class="footer">
  <svg class="topwave" width="1200" height="90" viewBox="0 0 1200 90"><path d="M0 0 H1200 V10 C800 90 400 70 0 20 Z" fill="#fff"/></svg>
  <div class="abs brand">VELTA CORE</div>
  <p class="about-text">Trusted wall and floor tilers for homes and businesses, covering pools, spas, paving, marble and bluestone across the region.</p>
  <h6 style="left:471px">Get in Touch</h6>
  <ul>
    <li><svg width="11" height="11" viewBox="0 0 24 24"><path fill="#fff" d="M6.6 10.8a15 15 0 0 0 6.6 6.6l2.2-2.2c.3-.3.7-.4 1-.2 1.1.4 2.3.6 3.6.6.6 0 1 .4 1 1V20c0 .6-.4 1-1 1A17 17 0 0 1 3 4c0-.6.4-1 1-1h3.5c.6 0 1 .4 1 1 0 1.3.2 2.5.6 3.6.1.3 0 .7-.2 1z"/></svg>Phone: +1 555 014 2687</li>
    <li><svg width="11" height="11" viewBox="0 0 12 12"><rect x="1" y="3" width="10" height="7" fill="#fff"/><rect x="3" y="0" width="6" height="3" fill="#fff"/></svg>Fax: +1 555 014 2688</li>
    <li><svg width="12" height="9" viewBox="0 0 26 20"><rect x="1" y="1" width="24" height="18" fill="none" stroke="#fff" stroke-width="2"/><path d="M1 1l12 10L25 1" fill="none" stroke="#fff" stroke-width="2"/></svg>Email: office@veltacore.example</li>
    <li><svg width="10" height="13" viewBox="0 0 10 14"><path d="M5 0a5 5 0 0 1 5 5c0 4-5 9-5 9S0 9 0 5a5 5 0 0 1 5-5z" fill="#fff"/><circle cx="5" cy="5" r="2" fill="#1a1a1a"/></svg>Adress: 48 Harbour Lane, Southbank, Australia</li>
  </ul>
  <h6 style="left:812px">Newsletter</h6>
  <div class="mail">Email ID</div>
  <div class="subscribe">SUBSCRIBE</div>
  <div class="rule"></div>
  <div class="copy">Copyright © 2017 Velta Core . All Rights Reserved.</div>
  <div class="links"><span>Home</span><span>|</span><span>Privacy &amp; Policy</span><span>|</span><span>FAQs</span><span>|</span><span>CSS</span></div>
</footer>

</body>
</html>
```